Business Card for Brevel Coatings

We need a simple, yet out standing business card for our painting company.

Target Market(s)

wealthy; high-end neighborhoods, and businesses

Industry/Entity Type

Painting

Contact Information for Business Card

Name:
Doran Vask

Email:
d.vask@brevel-coatings.com

Website:
Brevel-coatings.com

Phone Number:
(555) 416-9073

Font styles to use
Serif
Sans Serif

Requirements
Must have
• slogan "making change simple"
Should not have
• A title attached to the name on the card

```html
<!DOCTYPE html>
<html lang="en">
<head>
<meta charset="utf-8">
<title>Brevel Coatings — Business Card</title>
<link rel="stylesheet" href="https://fonts.googleapis.com/css2?family=Cinzel:wght@600;700&family=Open+Sans:wght@400&display=swap">
<style>
  :root {
    --backdrop: #cadfd3;
    --card: #ffffff;
    --forest: #2e5512;
    --lime: #9fcf1c;
    --card-shadow: rgba(40, 70, 55, 0.18);
  }
  * { box-sizing: border-box; margin: 0; padding: 0; }
  html, body {
    width: 1200px;
    height: 1000px;
    overflow: hidden;
  }
  body {
    background: var(--backdrop);
    position: relative;
    font-family: "Open Sans", sans-serif;
  }
  .card {
    position: absolute;
    width: 600px;
    height: 340px;
    background: var(--card);
    border-radius: 34px;
    box-shadow: 0 10px 28px var(--card-shadow);
  }
  .card--back { left: 470px; top: 110px; }
  .card--front { left: 130px; top: 520px; }

  /* Back: brand lockup centred */
  .brand-lockup {
    position: absolute;
    inset: 0;
    display: flex;
    align-items: center;
    justify-content: center;
    gap: 22px;
  }
  .brand-mark {
    width: 58px;
    height: 58px;
    background: var(--lime);
    flex: none;
  }
  .brand-text {
    display: flex;
    flex-direction: column;
    align-items: flex-start;
  }
  .brand-name {
    font-family: "Cinzel", serif;
    font-weight: 700;
    color: var(--forest);
    font-size: 38px;
    line-height: 1.1;
    letter-spacing: 1px;
  }
  .brand-slogan {
    color: var(--lime);
    font-size: 15px;
    line-height: 1.3;
    letter-spacing: 4px;
    text-transform: uppercase;
    margin-top: 4px;
  }

  /* Front: mark left, details right */
  .front-mark {
    position: absolute;
    left: 90px;
    top: 100px;
    width: 140px;
    height: 140px;
    background: var(--lime);
  }
  .details {
    position: absolute;
    left: 270px;
    top: 64px;
    display: flex;
    flex-direction: column;
    align-items: flex-start;
  }
  .details__company {
    font-family: "Cinzel", serif;
    font-weight: 700;
    color: var(--forest);
    font-size: 22px;
    line-height: 1.1;
    margin-bottom: 8px;
  }
  .details__person {
    font-family: "Cinzel", serif;
    font-weight: 700;
    color: var(--forest);
    font-size: 32px;
    line-height: 1.1;
    margin-bottom: 6px;
  }
  .details__line {
    color: var(--lime);
    font-size: 19px;
    line-height: 1.35;
  }
  .details__phone {
    color: var(--lime);
    font-size: 25px;
    line-height: 1.3;
    letter-spacing: 0.5px;
  }
  .details__slogan {
    color: var(--forest);
    font-size: 14px;
    line-height: 1.3;
    letter-spacing: 3px;
    text-transform: uppercase;
    margin-top: 10px;
  }
</style>
</head>
<body>
  <section class="card card--back" aria-label="Card back">
    <div class="brand-lockup">
      <div class="brand-mark"></div>
      <div class="brand-text">
        <div class="brand-name">Brevel Coatings</div>
        <div class="brand-slogan">making change simple</div>
      </div>
    </div>
  </section>

  <section class="card card--front" aria-label="Card front">
    <div class="front-mark"></div>
    <div class="details">
      <div class="details__company">Brevel Coatings</div>
      <div class="details__person">Doran Vask</div>
      <div class="details__line">d.vask@brevel-coatings.com</div>
      <div class="details__line">www.brevel-coatings.com</div>
      <div class="details__phone">(555) 416-9073</div>
      <div class="details__slogan">making change simple</div>
    </div>
  </section>
</body>
</html>
```